Long term Care Provider Conference

Banner for LTC providers to know that they can rely on us to deliver high value, cost efficient, professional back office support to streamline operations, improve and maintain compliance with administrative and or nursing solutions for their agency.

Want to update the wording

```html
<!DOCTYPE html>
<html lang="en">
<head>
<meta charset="utf-8">
<title>Nuvia Care – Conference Banner</title>
<link rel="stylesheet" href="https://fonts.googleapis.com/css2?family=Poppins:wght@400;500;600;700;800&display=swap">
<style>
  :root {
    --stage: #5f7371;
    --paper: #ffffff;
    --mist: #e6f6f6;
    --teal: #4a8d93;
    --teal-soft: #9fd9d8;
    --ink: #2f3538;
    --charcoal: #363c3f;
    --taupe: #cbbfba;
    --grey-icon: #a4a4a4;
    --white: #ffffff;
  }
  * { box-sizing: border-box; margin: 0; padding: 0; }
  html, body {
    width: 1200px; height: 2400px; overflow: hidden;
    background: var(--stage);
    font-family: "Poppins", sans-serif;
  }
  .banner {
    position: absolute; left: 40px; top: 589px;
    width: 1120px; height: 1222px; overflow: hidden;
    background: linear-gradient(180deg, var(--mist) 0%, var(--paper) 28%, var(--paper) 78%, #f1fbfb 100%);
    box-shadow: 0 20px 50px rgba(0,0,0,.3);
  }
  .eyebrow {
    position: absolute; left: 57px; top: 82px;
    font-size: 29px; font-weight: 500; letter-spacing: 13px; color: var(--ink);
  }
  .headline { position: absolute; left: 55px; top: 118px; color: var(--ink); }
  .headline .lead {
    display: block; font-size: 86px; font-weight: 700; color: var(--teal);
    line-height: 1; letter-spacing: -1px;
  }
  .headline .line { display: block; font-size: 60px; line-height: 66px; font-weight: 400; }
  .headline strong { font-weight: 800; }
  .brand {
    position: absolute; left: 640px; top: 68px;
    display: flex; align-items: center; gap: 20px;
  }
  .brand-dot { width: 92px; height: 92px; border-radius: 50%; background: var(--teal); }
  .brand-name { font-size: 60px; font-weight: 600; color: var(--charcoal); letter-spacing: -1px; }
  .photo-backdrop { position: absolute; left: 0; top: 0; }
  .photo {
    position: absolute; left: 545px; top: 231px; width: 550px; height: 550px; border-radius: 50%;
    background: radial-gradient(circle at 60% 55%, #e6e2df 0%, #c9c5c2 45%, #6f7a7c 100%);
  }
  .pill {
    position: absolute; display: flex; align-items: center; gap: 18px;
    border-radius: 40px; font-weight: 700; text-transform: uppercase;
  }
  .pill svg { flex: none; }
  .pill-value { left: 60px; top: 504px; width: 395px; height: 73px; padding-left: 24px; background: var(--taupe); color: var(--ink); font-size: 36px; }
  .pill-cost { left: 56px; top: 592px; width: 411px; height: 68px; padding-left: 24px; background: var(--charcoal); color: var(--white); font-size: 36px; }
  .feature { position: absolute; left: 66px; display: flex; align-items: center; gap: 24px; }
  .feature-icon { flex: none; width: 74px; height: 74px; }
  .feature-text { font-size: 22px; line-height: 28px; color: var(--ink); }
  .feature-office { top: 699px; }
  .feature-compliance { top: 809px; }
  .wave-field { position: absolute; left: 0; bottom: 0; width: 1120px; height: 290px; }
  .url {
    position: absolute; left: 170px; top: 1022px; width: 779px; height: 80px;
    border-radius: 40px; background: var(--charcoal); color: var(--white);
    display: flex; align-items: center; justify-content: center;
    font-size: 44px; font-weight: 700; letter-spacing: 12px;
    box-shadow: 0 16px 24px rgba(0,0,0,.18);
  }
</style>
</head>
<body>
  <section class="banner">
    <svg class="wave-field" viewBox="0 0 1120 290" role="img" aria-label="Soft teal flowing line pattern along the bottom">
      <defs>
        <linearGradient id="waveTint" x1="0" y1="0" x2="0" y2="1">
          <stop offset="0" stop-color="#c9efee" stop-opacity="0"/>
          <stop offset="1" stop-color="#c9efee" stop-opacity=".9"/>
        </linearGradient>
      </defs>
      <path d="M0 110 C250 240 500 20 760 90 S1040 80 1120 60 V290 H0 Z" fill="url(#waveTint)"/>
    </svg>

    <svg class="photo-backdrop" width="1120" height="1222" aria-hidden="true">
      <path d="M960 300 C1040 320 1060 400 1020 460 L940 420 Z" fill="var(--teal)"/>
      <path d="M1060 430 C1090 420 1110 418 1120 418 V520 L1060 500 Z" fill="var(--teal)"/>
    </svg>
    <div class="photo" role="img" aria-label="Photo of a smiling support agent with a headset working at a computer in an office"></div>

    <p class="eyebrow">TRANSFORMING</p>
    <h1 class="headline">
      <span class="lead">Healthcare,</span>
      <span class="line">with <strong>expert</strong></span>
      <span class="line"><strong>virtual</strong></span>
      <span class="line"><strong>assistant</strong></span>
      <span class="line">solutions</span>
    </h1>

    <div class="brand">
      <span class="brand-dot"></span>
      <span class="brand-name">Nuvia Care</span>
    </div>

    <div class="pill pill-value">
      <svg width="34" height="34" viewBox="0 0 34 34"><circle cx="17" cy="17" r="14" fill="none" stroke="#fff" stroke-width="3"/><path d="M11 17.5l4 4 8-8" fill="none" stroke="#fff" stroke-width="3" stroke-linecap="round" stroke-linejoin="round"/></svg>
      High Value
    </div>
    <div class="pill pill-cost">
      <svg width="34" height="34" viewBox="0 0 34 34"><circle cx="17" cy="17" r="14" fill="none" stroke="var(--teal)" stroke-width="3"/><path d="M11 17.5l4 4 8-8" fill="none" stroke="var(--teal)" stroke-width="3" stroke-linecap="round" stroke-linejoin="round"/></svg>
      Cost Efficient
    </div>

    <div class="feature feature-office">
      <svg class="feature-icon" viewBox="0 0 74 74" aria-hidden="true"><circle cx="37" cy="37" r="37" fill="var(--grey-icon)"/><rect x="20" y="29" width="34" height="24" rx="3" fill="#fff"/><rect x="30" y="23" width="14" height="8" rx="2" fill="none" stroke="#fff" stroke-width="3"/></svg>
      <p class="feature-text">We deliver professional back office<br>support to streamline operations.</p>
    </div>
    <div class="feature feature-compliance">
      <svg class="feature-icon" viewBox="0 0 74 74" aria-hidden="true"><circle cx="37" cy="37" r="37" fill="var(--grey-icon)"/><rect x="23" y="19" width="28" height="36" rx="3" fill="#fff"/><path d="M29 37l5 5 10-10" fill="none" stroke="var(--grey-icon)" stroke-width="3.5" stroke-linecap="round" stroke-linejoin="round"/></svg>
      <p class="feature-text">Improve and maintain compliance with administrative<br>and or nursing solutions.</p>
    </div>

    <div class="url">www.nuvia-care.com</div>
  </section>
</body>
</html>
```